Website design 5 pages + short Video + basic graphic optimization for a luxury Homestay - Resort website

I just need the website design for the main pages and optimised graphic images. The website will be mainly based on the following single-page scroll theme.

https://marshfieldthemes.com/demo/guesthouse-one-page/
FIGMA Templates https://marshfieldthemes.com/free-figma-design-files-for-hotel-and-vacation-rentals/
You can use these templates as a starting point but create something unique and luxurious.

Find all graphics files here :
1 https://www.stashcrate.net/sc/q8k517wp2ve4r7h/AAKP_Rmuvq53bx907Lqtcfw2e
2 https://www.stashcrate.net/sh/wrtmn48kdeyzqo/AAR7HunPLE93tWxM5NS2jobke?dl=0

The following is the output :
1. Create website design ( Output high-quality PSD and JPEG files )
a. Homepage ( Example https://marshfieldthemes.com/demo/countryside2/ )
b. Blog ( Example https://marshfieldthemes.com/demo/countryside2/blog-2/ )
c. Packages ….. ( Example xxxxx )
d. Room ( Example https://marshfieldthemes.com/demo/guesthouse-one-page/accommodation/kelwyn/ )
e. About us ( Example xxxxx )
f. Contact with embedded google maps ( Example https://marshfieldthemes.com/demo/hotelclassic/contact-2/ )

2. Short Video edit – 30 to 50 seconds

3. Optimise graphics for all pages and galleries ready to be used in the website ( Output high-quality JPEG files )

```html
<!DOCTYPE html>
<html lang="en">
<head>
<meta charset="utf-8">
<title>Lantana Ridge — Countryside Eco Stay</title>
<link href="https://fonts.googleapis.com/css2?family=Nunito+Sans:wght@400;600;700;800&family=Lora:wght@400;500&display=swap" rel="stylesheet">
<style>
:root{
  --gold:#f6b732;
  --band:#fbc55a;
  --dark:#1e1e1e;
  --footer:#25252b;
  --footer-deep:#1b1b20;
  --ink:#1f1f1f;
  --muted:#6b6b6b;
  --line:#e4e4e4;
  --soft:#f4f4f4;
  --white:#ffffff;
  --leaf:#3f6b2e;
  --leaf-deep:#22401c;
  --teal:#1fa88e;
}
*{box-sizing:border-box;margin:0;padding:0}
html,body{width:1200px;height:5217px;overflow:hidden}
body{font-family:"Nunito Sans",Arial,sans-serif;color:var(--ink);background:var(--white);position:relative}
section,header,footer{position:absolute;left:0;width:1200px;overflow:hidden}
.abs{position:absolute}
.eyebrow{font-family:"Lora",Georgia,serif;color:var(--gold);font-size:19px;font-weight:400}
.heading{font-weight:800;font-size:29px;line-height:36px;color:var(--ink)}
.body-text{font-size:11.5px;line-height:19px;color:var(--muted)}
.photo{position:absolute}
.btn{position:absolute;display:flex;align-items:center;justify-content:center;font-size:11px;font-weight:700}

/* header */
.site-header{top:0;height:61px;background:var(--dark)}
.brand{left:150px;top:16px;font-family:"Lora",Georgia,serif;font-size:22px;color:var(--gold)}
.nav{left:462px;top:22px;display:flex;gap:30px;font-size:12px;font-weight:600;color:var(--white)}
.nav .active{color:var(--gold)}
.social-dots{left:868px;top:23px;display:flex;gap:16px}
.social-dots span{width:14px;height:14px;border-radius:50%;border:2px solid var(--white)}
.book-now{left:972px;top:14px;width:94px;height:32px;background:var(--gold);color:var(--ink)}

/* hero */
.hero{top:61px;height:519px}
.hero-bg{left:0;top:0;width:1200px;height:519px;background:linear-gradient(180deg,#7f9b9a 0%,#557b4b 30%,#3a5e2d 65%,#2b4722 100%)}
.hero-shade{left:0;top:0;width:1200px;height:519px;background:rgba(0,0,0,.25)}
.hero-kicker{left:0;width:1200px;top:104px;text-align:center;font-family:"Lora",Georgia,serif;font-size:21px;color:var(--white)}
.hero-title{left:0;width:1200px;top:142px;text-align:center;font-size:42px;line-height:50px;font-weight:800;color:var(--gold)}
.hero-text{left:370px;width:460px;top:259px;text-align:center;font-size:11px;line-height:19px;color:var(--white)}
.hero-btn{left:521px;top:335px;width:106px;height:36px;background:var(--white);color:var(--ink)}
.play{width:38px;height:38px;border-radius:50%;background:var(--white);display:flex;align-items:center;justify-content:center}

/* about */
.about{top:580px;height:480px}
.about .eyebrow{left:136px;top:81px}
.about .heading{left:136px;top:118px;width:360px}
.about .body-text{left:136px;top:240px;width:350px}
.read-more{position:absolute;font-size:11px;font-weight:800;color:var(--ink)}
.about .read-more{left:136px;top:348px}

/* services */
.services{top:1060px;height:562px}
.services-bg{left:0;top:0;width:1200px;height:562px;background:linear-gradient(180deg,#2a2018,#3a2a1b 50%,#1c1610)}
.services-shade{left:0;top:0;width:1200px;height:562px;background:rgba(0,0,0,.35)}
.services .eyebrow{left:0;width:1200px;top:71px;text-align:center;font-size:18px}
.services .heading{left:0;width:1200px;top:98px;text-align:center;color:var(--white);font-size:28px}
.service-card{position:absolute;top:168px;width:222px;height:296px;background:var(--white);text-align:center}
.service-card .ring{position:absolute;left:49px;top:18px;width:124px;height:124px;border-radius:50%;border:2px solid var(--gold);padding:6px}
.service-card .ring div{width:100%;height:100%;border-radius:50%}
.service-card h3{position:absolute;left:0;width:222px;top:184px;font-family:"Lora",Georgia,serif;font-size:13px;font-weight:500}
.service-card p{position:absolute;left:20px;width:182px;top:210px;font-size:10px;line-height:17px;color:var(--muted)}
.service-card .read-more{left:0;width:222px;top:266px;font-size:10px;font-weight:600;color:var(--muted)}
.arrow-dot{position:absolute;width:30px;height:30px;border-radius:50%;background:var(--white);display:flex;align-items:center;justify-content:center}

/* callcenter */
.call-band{top:1622px;height:99px;background:var(--band)}
.call-band .label{left:134px;top:22px;font-family:"Lora",Georgia,serif;font-size:19px;color:var(--white)}
.call-band .ask{left:134px;top:50px;font-size:20px;font-weight:800;color:var(--ink)}
.call-band .phone{left:566px;top:32px;font-size:26px;font-weight:800;color:var(--white)}
.call-band .contact{left:960px;top:32px;width:107px;height:38px;background:var(--ink);color:var(--white)}

/* amenities */
.amenities{top:1721px;height:667px}
.amenities .eyebrow{left:186px;top:108px}
.amenities .heading{left:186px;top:142px;width:330px;line-height:36px}
.amenities .intro{left:186px;top:260px;width:350px}
.perk{position:absolute;left:186px;width:364px;border-bottom:1px solid var(--line)}
.perk svg{position:absolute;left:2px;top:6px}
.perk h4{position:absolute;left:56px;top:0;font-size:10px;font-weight:800}
.perk p{position:absolute;left:56px;top:18px;font-size:11px;line-height:18px;color:#444;width:300px}

/* video banner */
.video-band{top:2388px;height:342px}
.video-bg{left:0;top:0;width:1200px;height:342px;background:linear-gradient(180deg,#2e3a23,#4d5d2f 45%,#3a4a25)}
.video-shade{left:0;top:0;width:1200px;height:342px;background:rgba(0,0,0,.45)}
.video-band .eyebrow{left:0;width:1200px;top:85px;text-align:center;font-size:18px}
.video-band .heading{left:0;width:1200px;top:124px;text-align:center;color:var(--white);font-size:25px;line-height:35px}

/* gallery */
.gallery{top:2730px;height:639px}
.gallery .eyebrow{left:0;width:1200px;top:88px;text-align:center;font-size:18px}
.gallery .heading{left:0;width:1200px;top:126px;text-align:center;font-size:26px}
.dots{position:absolute;display:flex;gap:5px}
.dots span{width:6px;height:6px;border-radius:50%;background:#444}
.dots span:first-child{background:var(--gold)}

/* booking */
.booking{top:3369px;height:410px;background:var(--dark)}
.booking .eyebrow{left:642px;top:68px;font-size:18px}
.booking .heading{left:642px;top:102px;color:var(--white);font-size:28px}
.booking .body-text{left:642px;top:155px;width:330px;color:#cfcfcf;font-size:10.5px}
.field{position:absolute;left:642px;width:334px;height:38px;border:1px solid #777;color:#bbb;font-size:10px;padding:12px 14px}
.field svg{position:absolute;right:12px;top:12px}
.check-btn{left:642px;top:322px;width:334px;height:38px;background:var(--white);color:var(--ink)}

/* rooms */
.rooms{top:3779px;height:733px}
.rooms .eyebrow{left:0;width:1200px;top:88px;text-align:center;font-size:18px}
.rooms .heading{left:0;width:1200px;top:128px;text-align:center;font-size:26px}
.room{position:absolute;top:228px;width:300px;height:520px}
.room .img{position:absolute;left:0;top:0;width:300px;height:288px}
.room .tag{position:absolute;left:22px;top:22px;padding:7px 14px;background:var(--band);font-size:9px;font-weight:700}
.room .price{position:absolute;right:0;top:242px;width:80px;height:46px;background:var(--white);border-radius:8px 0 0 0;text-align:center;font-size:9px;font-weight:800;padding-top:9px;line-height:13px}
.room h3{position:absolute;left:0;top:311px;font-size:12px;font-weight:800}
.room p{position:absolute;left:0;top:333px;width:270px;font-size:10.5px;line-height:18px;color:var(--muted)}
.room .cta{position:absolute;left:0;top:404px;width:118px;height:30px;border:1px solid #999;display:flex;align-items:center;justify-content:center;font-size:9.5px;font-weight:700}
.room .cta.filled{background:var(--band);border-color:var(--band)}
.nav-chev{position:absolute;top:134px;color:var(--white);font-size:18px}

/* testimonials */
.testimonials{top:4512px;height:379px;background:var(--soft)}
.testimonials .eyebrow{left:134px;top:145px;font-size:18px}
.testimonials .heading{left:134px;top:180px;font-size:28px}
.quote{position:absolute;top:55px;width:262px;height:233px;background:var(--white);text-align:center}
.quote .avatar{position:absolute;left:113px;top:-14px;width:36px;height:36px;border-radius:50%;background:#c9c2b8;border:2px solid var(--white)}
.quote .stars{position:absolute;left:0;width:262px;top:28px;color:var(--gold);font-size:13px;letter-spacing:2px}
.quote h5{position:absolute;left:0;width:262px;top:48px;font-family:"Lora",Georgia,serif;font-size:11px;font-weight:500}
.quote .role{position:absolute;left:0;width:262px;top:64px;font-size:8px;color:var(--gold)}
.quote p{position:absolute;left:22px;width:218px;top:90px;font-size:10px;line-height:17px;color:#888}

/* footer */
.site-footer{top:4891px;height:326px;background:var(--footer)}
.site-footer .brand{left:142px;top:62px}
.footer-about{left:134px;top:110px;width:230px;font-size:10px;line-height:18px;color:#c8c8c8}
.square-row{left:134px;top:172px;display:flex;gap:10px}
.square-row span{width:20px;height:20px;background:var(--gold)}
.f-col{position:absolute;top:72px}
.f-col h6{font-size:14px;font-weight:700;color:var(--gold);margin-bottom:16px}
.f-col li{list-style:none;font-size:10px;color:#dcdcdc;margin-bottom:22px}
.contact-li{display:flex;align-items:center;gap:10px}
.contact-li i{width:20px;height:20px;border-radius:50%;background:var(--gold);display:flex;align-items:center;justify-content:center}
.copyright{left:0;top:294px;width:1200px;height:32px;background:var(--footer-deep);text-align:center;font-size:10px;line-height:32px;color:#ddd}
</style>
</head>
<body>

<header class="site-header">
  <div class="abs brand">Lantana Ridge</div>
  <nav class="abs nav"><span class="active">Home</span><span>Pages</span><span>Features</span><span>Blog</span><span>Contact</span></nav>
  <div class="abs social-dots"><span></span><span></span><span></span></div>
  <div class="btn book-now">Book Now</div>
</header>

<section class="hero">
  <div class="photo hero-bg" role="img" aria-label="Pine forest hillside with a green-roofed cottage among the trees"></div>
  <div class="photo hero-shade"></div>
  <div class="abs hero-kicker">The perfect place to escape</div>
  <h1 class="abs hero-title">Experience something new<br>every moment</h1>
  <p class="abs hero-text">Welcome to our countryside vacation rental! Our property is the perfect place to escape the hustle and bustle of city life and enjoy a relaxing and peaceful vacation.</p>
  <div class="btn hero-btn">Book Now</div>
  <div class="abs play" style="left:640px;top:334px"><svg width="12" height="14" viewBox="0 0 12 14"><path d="M1 1l10 6-10 6z" fill="#f6b732"/></svg></div>
</section>

<section class="about">
  <div class="abs eyebrow">Escape The City</div>
  <h2 class="abs heading">Welcome to the quiet eco house. enjoy and get inspired.</h2>
  <p class="abs body-text">Our spacious and comfortable home is perfect for large groups, and we have plenty of outdoor space for kids to run and play. we also have a private pool and hot tub, perfect for relaxing after a long day of hiking or exploring the local area.</p>
  <div class="read-more">Read More &rarr;</div>
  <div class="photo" role="img" aria-label="Timber A-frame cabin lit at night" style="left:688px;top:68px;width:376px;height:288px;background:linear-gradient(135deg,#2b2118,#6a4a22 55%,#1a1510);box-shadow:0 8px 24px rgba(0,0,0,.18)"></div>
  <div class="photo" role="img" aria-label="Green-roofed cottage on a grassy hillside" style="left:551px;top:115px;width:266px;height:166px;background:linear-gradient(180deg,#8fb8d9,#4f8a3a 55%,#2f5a24);border:4px solid #fff"></div>
  <div class="photo" role="img" aria-label="Cottage seen from above among pine trees" style="left:648px;top:225px;width:322px;height:176px;background:linear-gradient(180deg,#a9c9e6,#5d9047 50%,#2e5524);border:4px solid #fff"></div>
</section>

<section class="services">
  <div class="photo services-bg" role="img" aria-label="Cabin interior at dusk with warm timber beams"></div>
  <div class="photo services-shade"></div>
  <div class="abs eyebrow">Your Services</div>
  <h2 class="abs heading">At Your Service</h2>
  <div class="arrow-dot" style="left:82px;top:301px"><svg width="10" height="10"><path d="M9 5H1M4 2L1 5l3 3" stroke="#222" fill="none" stroke-width="1.4"/></svg></div>
  <div class="arrow-dot" style="left:1086px;top:301px"><svg width="10" height="10"><path d="M1 5h8M6 2l3 3-3 3" stroke="#222" fill="none" stroke-width="1.4"/></svg></div>

  <article class="service-card" style="left:132px">
    <div class="ring"><div role="img" aria-label="Row of laundry machines" style="background:linear-gradient(135deg,#c4622e,#6b3a22)"></div></div>
    <h3>Laundry Service</h3><p>There Are Laundry Facilities And Kitchen Facilities For Guests To Use.</p>
    <div class="read-more">Read More &rarr;</div>
  </article>
  <article class="service-card" style="left:371px">
    <div class="ring"><div role="img" aria-label="Breakfast dishes on a table" style="background:linear-gradient(135deg,#e7d8c0,#b77a3e)"></div></div>
    <h3>Breakfast Service</h3><p>The hostel offers a free breakfast every morning</p>
    <div class="read-more">Read More &rarr;</div>
  </article>
  <article class="service-card" style="left:608px">
    <div class="ring"><div role="img" aria-label="Glasses raised at a bar" style="background:linear-gradient(135deg,#8a98a8,#3d4650)"></div></div>
    <h3>Local C And Wines</h3><p>There is also a bar on-site that serves local beers and wines</p>
    <div class="read-more">Read More &rarr;</div>
  </article>
  <article class="service-card" style="left:845px">
    <div class="ring"><div role="img" aria-label="Orange shuttle van" style="background:linear-gradient(180deg,#cfe3f1,#f0a93a 55%,#e3892a)"></div></div>
    <h3>Shuttle Service</h3><p>Avoid the hassle and take advantage of our complimentary</p>
    <div class="read-more">Read More &rarr;</div>
  </article>
</section>

<section class="call-band">
  <div class="abs label">24/7 Callcenter</div>
  <div class="abs ask">Need Any Services ?</div>
  <svg class="abs" style="left:516px;top:28px" width="40" height="40" viewBox="0 0 40 40"><path d="M9 5l6 0 3 8-4 3c2 5 6 9 11 11l3-4 8 3v6c0 2-2 4-4 4C17 36 4 23 5 9c0-2 2-4 4-4z" fill="none" stroke="#1f1f1f" stroke-width="2.2"/></svg>
  <div class="abs phone">0-800-555-0-155</div>
  <div class="btn contact">Contact Us</div>
</section>

<section class="amenities">
  <div class="abs eyebrow">Amenities &amp; Benefits</div>
  <h2 class="abs heading">Surrounded By Nature, Stunning Views Of The Countryside.</h2>
  <p class="abs body-text intro">Country rentals often come with extra amenities, such as pools, tennis courts, and hiking trails. this can be a great way to enjoy your vacation without having to leave the property.</p>
  <div class="perk" style="top:370px;height:68px">
    <svg width="30" height="26" viewBox="0 0 30 26"><path d="M15 2L2 13h4v11h7v-7h4v7h7V13h4z" fill="#f6b732"/></svg>
    <h4>Entire Home</h4><p>You'll Have The Tiny House To Yourself.</p>
  </div>
  <div class="perk" style="top:448px;height:84px">
    <svg width="30" height="30" viewBox="0 0 30 30"><path d="M22 3l3 3-9 9-3-3z M12 13l5 5-3 8H4l2-6z" fill="#f6b732"/></svg>
    <h4>Enhanced Clean</h4><p>This Host Committed To HostHaven's 5-Step Enhanced Cleaning Process</p>
  </div>
  <div class="perk" style="top:543px;height:40px;border:none">
    <svg width="26" height="28" viewBox="0 0 26 28"><path d="M13 2l10 4v8c0 6-5 10-10 12C8 24 3 20 3 14V6z" fill="#f6b732"/><path d="M8 14l4 4 6-7" stroke="#fff" stroke-width="2" fill="none"/></svg>
    <h4>Self Check-In</h4><p>Check Yourself In With The Lockbox.</p>
  </div>
  <div class="photo" role="img" aria-label="Stone path through woods leading to a teal-roofed cabin" style="left:612px;top:75px;width:400px;height:517px;background:linear-gradient(180deg,#7aa850,#3d6a2a 45%,#2a3f1f)"></div>
  <div class="photo" role="img" aria-label="Teal-roofed cabin surrounded by trees" style="left:922px;top:292px;width:205px;height:269px;border-radius:14px;border:5px solid #fff;background:linear-gradient(180deg,#6f9a46,#2b8f7a 55%,#2c4d22)"></div>
</section>

<section class="video-band">
  <div class="photo video-bg" role="img" aria-label="A-frame farmhouse roof against green hills"></div>
  <div class="photo video-shade"></div>
  <div class="abs eyebrow">A Charming Farmhouse</div>
  <h2 class="abs heading">Looking For A Relaxing Country<br>Vacation Rental?</h2>
  <div class="abs play" style="left:578px;top:243px;width:44px;height:44px"><svg width="13" height="15" viewBox="0 0 12 14"><path d="M1 1l10 6-10 6z" fill="#222"/></svg></div>
</section>

<section class="gallery">
  <svg class="abs" style="left:0;top:140px" width="1200" height="330" viewBox="0 0 1200 330"><path d="M0 330L90 120 180 330z M1040 330L1110 150 1200 300z" fill="#f3f3f3"/></svg>
  <div class="abs eyebrow">About Countryside</div>
  <h2 class="abs heading">A Secret Garden In The Countryside</h2>
  <div class="photo" role="img" aria-label="Tall pines with sunlight over a garden path" style="left:103px;top:203px;width:240px;height:276px;background:linear-gradient(180deg,#a8cbe8,#4f7f3a 55%,#2b4a22)"></div>
  <div class="photo" role="img" aria-label="Guests walking across a grassy meadow" style="left:359px;top:248px;width:240px;height:275px;background:linear-gradient(180deg,#7fb0e3,#6aa04a 50%,#4a7a30)"></div>
  <div class="photo" role="img" aria-label="Dense green trees around the property" style="left:616px;top:203px;width:240px;height:276px;background:linear-gradient(180deg,#5f9840,#3a6c2a 60%,#294b1e)"></div>
  <div class="photo" role="img" aria-label="Teal-roofed cottage in a green valley" style="left:874px;top:248px;width:240px;height:275px;background:linear-gradient(180deg,#6da548,#1f9c86 55%,#33592a)"></div>
  <div class="abs" style="left:88px;top:325px;width:30px;height:30px;border-radius:50%;background:var(--gold);display:flex;align-items:center;justify-content:center"><svg width="10" height="10"><path d="M9 5H1M4 2L1 5l3 3" stroke="#fff" fill="none" stroke-width="1.4"/></svg></div>
  <div class="abs" style="left:1097px;top:370px;width:30px;height:30px;border-radius:50%;background:var(--gold);display:flex;align-items:center;justify-content:center"><svg width="10" height="10"><path d="M1 5h8M6 2l3 3-3 3" stroke="#fff" fill="none" stroke-width="1.4"/></svg></div>
  <div class="dots" style="left:582px;top:560px"><span></span><span></span><span></span><span></span></div>
</section>

<section class="booking">
  <div class="photo" role="img" aria-label="Close view of a teal A-frame roof among greenery" style="left:0;top:0;width:563px;height:410px;background:linear-gradient(160deg,#8fb66a,#1fa88e 45%,#2c5a26)"></div>
  <div class="abs eyebrow">Booking</div>
  <h2 class="abs heading">Book Today</h2>
  <p class="abs body-text">This house is one of the favorite houses of our clients, so they talk about it and leave reviews.</p>
  <div class="field" style="top:218px">Check-In Date<svg width="12" height="12"><rect x="1" y="2" width="10" height="9" fill="none" stroke="#bbb"/><path d="M1 5h10" stroke="#bbb"/></svg></div>
  <div class="field" style="top:269px">Check-Out Date<svg width="12" height="12"><rect x="1" y="2" width="10" height="9" fill="none" stroke="#bbb"/><path d="M1 5h10" stroke="#bbb"/></svg></div>
  <div class="btn check-btn">Check Availability</div>
  <svg class="abs" style="left:1016px;top:250px" width="140" height="130" viewBox="0 0 140 130"><path d="M70 8L6 66h16v60h96V66h16z" fill="#2b2b2b"/><rect x="72" y="70" width="28" height="28" fill="#1e1e1e"/></svg>
</section>

<section class="rooms">
  <div class="abs eyebrow">Amazing Views!</div>
  <h2 class="abs heading">Equipped With All The Necessary<br>Amenities</h2>
  <article class="room" style="left:134px">
    <div class="img" role="img" aria-label="Terraced green fields seen from a cottage porch" style="background:linear-gradient(180deg,#6f9a4a,#4b7a34 55%,#2a4a20)"></div>
    <div class="tag">Private Porch</div><span class="nav-chev" style="left:14px">&lsaquo;</span><span class="nav-chev" style="right:14px">&rsaquo;</span>
    <div class="price">$399<br>/Night</div>
    <h3>THE COTTAGE</h3><p>This room is located in a cottage on the water. it has a king sized bed, a Jacuzzi tub, and a private porch.</p>
    <div class="cta">Check Availability</div>
  </article>
  <article class="room" style="left:450px">
    <div class="img" role="img" aria-label="Green-roofed farmhouse under blue sky" style="background:linear-gradient(180deg,#8fb9e0,#4e8a3c 50%,#2d5224)"></div>
    <div class="tag">Private Porch</div><span class="nav-chev" style="left:14px">&lsaquo;</span><span class="nav-chev" style="right:14px">&rsaquo;</span>
    <div class="price">$399<br>/Night</div>
    <h3>THE FARMHOUSE</h3><p>This room is located in a cottage on the water. it has a king sized bed, a Jacuzzi tub, and a private porch.</p>
    <div class="cta filled">Check Availability</div>
  </article>
  <article class="room" style="left:766px">
    <div class="img" role="img" aria-label="Cabin roof hidden among leafy trees" style="background:linear-gradient(180deg,#6c9d45,#3f7430 55%,#24441b)"></div>
    <div class="tag">Private Porch</div><span class="nav-chev" style="left:14px">&lsaquo;</span><span class="nav-chev" style="right:14px">&rsaquo;</span>
    <div class="price">$399<br>/Night</div>
    <h3>THE CABIN</h3><p>This room is located in a cottage on the water. it has a king sized bed, a Jacuzzi tub, and a private porch.</p>
    <div class="cta">Check Availability</div>
  </article>
</section>

<section class="testimonials">
  <div class="abs eyebrow">Testimonial</div>
  <h2 class="abs heading">A Few Words From<br>Our Happy Clients</h2>
  <article class="quote" style="left:523px">
    <div class="avatar" role="img" aria-label="Guest portrait"></div>
    <div class="stars">★★★★★</div><h5>Clara Henley</h5><div class="role">Adventurer</div>
    <p>"When you are designing with Lorem Ipsum you diminish the importance of the copy by lowering it to the same level as any other visual element.</p>
  </article>
  <article class="quote" style="left:806px">
    <div class="avatar" role="img" aria-label="Guest portrait"></div>
    <div class="stars">★★★★★</div><h5>Clara Henley</h5><div class="role">Adventurer</div>
    <p>"When you are designing with Lorem Ipsum you diminish the importance of the copy by lowering it to the same level as any other visual element.</p>
  </article>
  <div class="dots" style="left:774px;top:312px"><span></span><span></span><span></span><span></span></div>
</section>

<footer class="site-footer">
  <div class="abs brand">Lantana Ridge</div>
  <p class="abs footer-about">When you are designing with Lorem Ipsum you diminish the importance of the copy by lowering it to the same level</p>
  <div class="abs square-row"><span></span><span></span><span></span><span></span></div>
  <div class="f-col" style="left:452px"><h6>Explore</h6><ul><li>Home</li><li>About</li><li>Services</li><li>Blog</li></ul></div>
  <div class="f-col" style="left:597px"><h6>Quick link</h6><ul><li>Our Place</li><li>Our Menu</li><li>Why Us</li><li>Room Styles</li></ul></div>
  <div class="f-col" style="left:784px"><h6>Contact us</h6><ul>
    <li class="contact-li"><i><svg width="10" height="8"><rect x=".5" y=".5" width="9" height="7" fill="none" stroke="#222"/><path d="M.5.5l4.5 4 4.5-4" stroke="#222" fill="none"/></svg></i>stay@lantanaridge.com</li>
    <li class="contact-li"><i><svg width="10" height="10" viewBox="0 0 10 10"><path d="M2 1h2l1 2-1 1c1 1 2 2 3 3l1-1 2 1v2c-5 0-9-4-8-8z" fill="#222"/></svg></i>1-800-555-0142</li>
    <li class="contact-li"><i><svg width="8" height="11" viewBox="0 0 8 11"><path d="M4 0a4 4 0 0 1 4 4c0 3-4 7-4 7S0 7 0 4a4 4 0 0 1 4-4z" fill="#222"/><circle cx="4" cy="4" r="1.5" fill="#f6b732"/></svg></i>Hollin Vale, Norland, 40217</li>
  </ul></div>
  <div class="abs copyright">Copyright. All right reserved.</div>
</footer>

</body>
</html>
```